Kioskwave Entertainment Stationary

Start up company requires matching stationary templates for Business Cards, letterhead and 'With Compliments' slips. The final design should keep with the style of our kiosk design, investor brochure and other collateral.

```html
<!DOCTYPE html>
<html lang="en">
<head>
<meta charset="utf-8">
<title>Kioskwave Entertainment Letterhead</title>
<link rel="stylesheet" href="https://fonts.googleapis.com/css2?family=Roboto+Condensed:wght@300;400;700&display=swap">
<style>
  :root {
    --backdrop: #e6e7e8;
    --paper: #f5f5f6;
    --brand-blue: #1269b0;
    --accent-lilac: #b9c1da;
    --tagline-grey: #cdd0d6;
    --tagline-strong: #aab4cf;
    --ink: #3a3d44;
    --white: #ffffff;
  }
  * { box-sizing: border-box; margin: 0; padding: 0; }
  html, body {
    width: 1200px; height: 795px; overflow: hidden;
    background: var(--backdrop);
    font-family: "Roboto Condensed", Arial, sans-serif;
  }
  .letterhead {
    position: absolute; left: 330px; top: 15px;
    width: 540px; height: 764px;
    background: var(--paper);
    box-shadow: 0 2px 10px rgba(0,0,0,0.12);
    overflow: hidden;
  }
  .brand {
    position: absolute; left: 42px; top: 112px;
    display: flex; align-items: center; gap: 8px;
    color: var(--brand-blue);
  }
  .brand-dot {
    width: 10px; height: 10px; border-radius: 50%;
    background: var(--brand-blue);
  }
  .brand-name {
    font-weight: 700; font-size: 18px; line-height: 1;
    text-transform: uppercase; letter-spacing: 0.5px;
  }
  .contact {
    position: absolute; left: 300px; top: 42px;
    color: var(--ink); font-size: 8px; line-height: 13px;
    font-style: normal;
  }
  .contact-title { font-weight: 700; letter-spacing: 2px; margin-bottom: 3px; }
  .contact-row { display: flex; align-items: center; gap: 6px; letter-spacing: 0.6px; }
  .contact-row svg { width: 8px; height: 8px; flex: none; }
  .world-map {
    position: absolute; left: 300px; top: 420px;
    width: 240px; height: 150px;
    background: radial-gradient(ellipse at 60% 45%, rgba(185,193,218,0.55), rgba(185,193,218,0) 70%);
  }
  .tagline {
    position: absolute; left: 38px; top: 600px;
    color: var(--tagline-grey); text-transform: uppercase;
    font-size: 27px; line-height: 0.95; font-weight: 300;
  }
  .tagline strong { color: var(--tagline-strong); font-weight: 700; }
  .footer-wave { position: absolute; left: 0; bottom: 0; width: 540px; height: 240px; }
  .website {
    position: absolute; left: 250px; top: 700px;
    color: var(--white); font-size: 10.5px; font-weight: 700;
    letter-spacing: 2.4px; text-transform: uppercase;
    transform: rotate(-12deg); transform-origin: left center;
  }
</style>
</head>
<body>
  <main class="letterhead">
    <div class="brand">
      <div class="brand-dot"></div>
      <div class="brand-name">Kioskwave Entertainment</div>
    </div>

    <address class="contact">
      <div class="contact-title">KIOSKWAVE</div>
      <div class="contact-row">
        <svg viewBox="0 0 10 10"><path d="M2 1h2l1 2-1 1c.6 1.2 1.4 2 2 2l1-1 2 1v2c-4 0-7-3-7-7z" fill="var(--brand-blue)"/></svg>
        555-010-1111
      </div>
      <div class="contact-row">
        <svg viewBox="0 0 10 10"><path d="M2 1h2l1 2-1 1c.6 1.2 1.4 2 2 2l1-1 2 1v2c-4 0-7-3-7-7z" fill="var(--brand-blue)"/></svg>
        555-010-2222
      </div>
      <div class="contact-row">
        <svg viewBox="0 0 10 10"><rect x="1" y="1" width="8" height="8" fill="none" stroke="var(--brand-blue)" stroke-width="1.4"/><rect x="3" y="3" width="4" height="2" fill="var(--brand-blue)"/></svg>
        555-010-3333
      </div>
      <div class="contact-row">
        <svg viewBox="0 0 10 10"><rect x="1" y="2" width="8" height="6" fill="none" stroke="var(--brand-blue)" stroke-width="1.2"/><path d="M1 2l4 3 4-3" fill="none" stroke="var(--brand-blue)" stroke-width="1.2"/></svg>
        hello@kioskwaveent.com
      </div>
    </address>

    <div class="world-map" role="img" aria-label="Faint dotted world map in pale lilac"></div>

    <p class="tagline">Technology built for<br><strong>Global</strong> expansion</p>

    <svg class="footer-wave" viewBox="0 0 540 240" preserveAspectRatio="none" aria-hidden="true">
      <path d="M0 232 C150 226 250 196 320 140 C390 84 450 66 540 56 L540 240 L0 240 Z" fill="var(--accent-lilac)"/>
      <path d="M0 240 L0 236 C160 232 262 204 334 148 C402 96 460 80 540 72 L540 240 Z" fill="var(--brand-blue)"/>
    </svg>

    <div class="website">www.kioskwaveent.com</div>
  </main>
</body>
</html>
```